Custom Home Page for our new Website

We need a custom home page designed for our new website. We are a successful local copier dealer who is rebuilding our website from scratch. We have decided on Wordpress as our CMS platform and have purchased the professional Corvel theme.

The custom homepage we want will be an imitation of the screen on latest model of copiers we carry. (A picture of this is attached.) the goal is to imitate this style while creating a unique, user-friendly, helpful portal to our website.

The winning entry will make the best transition between the menu structure of our current website (www.hlumo.net) and the new layout.

Target Market(s)

Our target market is small to medium sized businesses in the Southeast US. The users of our site are generally IT professionals looking for drivers/support, gatekeepers or other support staff placing service calls and supply orders or prospects looking for information about our company and products.

Requirements
Must have
• Clean design, no distracting elements
• Modern aesthetic
• A color palette that can be used as a basis for the Skin for the rest of the site (The site's look will be based on the winning homepage design.)
• Simple navigation
• Easy to read
• Easily viewed on both desktop and tablet sized screens
• Our logo
• Easily update-able
• Maximum of 4 of the large squares

```html
<!DOCTYPE html>
<html lang="en">
<head>
<meta charset="utf-8">
<title>Hlumo – Business Copiers/MFPs</title>
<link rel="stylesheet" href="https://fonts.googleapis.com/css2?family=Oswald:wght@300;400&family=Open+Sans:wght@400;600&family=Arimo:wght@700&display=swap">
<style>
  :root {
    --header-top: #231212;
    --header-bottom: #140a0a;
    --nav-bg: #080505;
    --red-core: #e31d1f;
    --red-mid: #8c1012;
    --red-deep: #2a0505;
    --dome: #000000;
    --white: #ffffff;
    --phone-grey: #b3b3b3;
    --accent: #e0191d;
    --footer-rule: #2b2b2b;
    --copy-grey: #d0d0d0;
  }
  * { margin: 0; padding: 0; box-sizing: border-box; }
  html, body { width: 1200px; height: 730px; overflow: hidden; background: #000; }
  .page { position: relative; width: 1200px; height: 730px; overflow: hidden;
    background: radial-gradient(ellipse 620px 470px at 600px 600px, var(--red-core) 0%, var(--red-mid) 45%, var(--red-deep) 100%); }

  .site-header { position: absolute; top: 0; left: 0; width: 1200px; height: 112px;
    background: linear-gradient(var(--header-top), var(--header-bottom)); }
  .brand { position: absolute; left: 162px; top: 30px; display: flex; align-items: center; gap: 12px; }
  .brand-dot { width: 46px; height: 46px; border-radius: 50%; background: var(--accent); }
  .brand-name { font-family: "Oswald", sans-serif; font-weight: 400; font-size: 40px; color: var(--white); line-height: 1; }
  .contact-lines { position: absolute; right: 130px; top: 39px; font-family: "Arimo", Arial, sans-serif;
    font-weight: 700; font-size: 15px; line-height: 19px; color: var(--phone-grey); }

  .main-nav { position: absolute; top: 112px; left: 0; width: 1200px; height: 39px; background: var(--nav-bg);
    display: flex; justify-content: center; gap: 0; padding-left: 30px; }
  .main-nav a { font-family: "Oswald", sans-serif; font-size: 18px; color: var(--white); text-decoration: none;
    padding: 7px 14px 0; height: 39px; position: relative; }
  .main-nav a.is-active::after { content: ""; position: absolute; left: 0; right: 0; bottom: 0; height: 3px; background: var(--accent); }

  .hero-title { position: absolute; left: 157px; top: 186px; font-family: "Oswald", sans-serif; font-weight: 400;
    font-size: 60px; line-height: 70px; color: var(--white); }
  .hero-text { position: absolute; left: 164px; top: 343px; width: 360px; font-family: "Open Sans", sans-serif;
    font-size: 11.5px; line-height: 18px; color: var(--white); }
  .read-more { position: absolute; left: 160px; top: 447px; width: 241px; height: 65px; border-radius: 8px;
    background: linear-gradient(#ef3a3c 0%, #d8181b 50%, #c01013 100%); border: 3px solid #e76a6b;
    font-family: "Open Sans", sans-serif; font-size: 30px; color: var(--white); text-align: center; line-height: 59px; }
  .product-shot { position: absolute; left: 656px; top: 182px; width: 394px; height: 348px;
    background: linear-gradient(160deg, #eeeeee, #bdbdbd); border-radius: 4px; }
  .slider-dots { position: absolute; left: 590px; top: 504px; display: flex; gap: 5px; }
  .slider-dots span { width: 11px; height: 11px; border-radius: 50%; background: #e8b0b0; }
  .slider-dots span.is-current { background: var(--white); }

  .dome { position: absolute; left: 0; top: 0; }
  .quick-links { position: absolute; left: 0; top: 580px; width: 1200px; }
  .quick-link { position: absolute; width: 200px; text-align: center; }
  .quick-link .label { display: block; margin-top: 8px; font-family: "Oswald", sans-serif; font-size: 19px; color: var(--white); }
  .quick-link .icon { height: 50px; display: flex; justify-content: center; align-items: flex-end; }
  .icon-brand { font-family: "Oswald", sans-serif; font-size: 26px; color: var(--white); line-height: 1; }
  .icon-copier { width: 64px; height: 50px; background: linear-gradient(#e0e0e0, #9e9e9e); }
  .icon-support { width: 38px; height: 48px; background: var(--white); border-radius: 19px 19px 6px 6px; }

  .footer-rule { position: absolute; left: 130px; top: 694px; width: 940px; height: 1px; background: var(--footer-rule); }
  .copyright { position: absolute; right: 138px; top: 705px; font-family: "Open Sans", sans-serif; font-size: 11px; color: var(--copy-grey); }
</style>
</head>
<body>
<div class="page">
  <header class="site-header">
    <div class="brand"><span class="brand-dot"></span><span class="brand-name">Hlumo</span></div>
    <div class="contact-lines">GREENVILLE 864.555.0142<br>CHARLOTTE&nbsp; 980.555.0187</div>
  </header>

  <nav class="main-nav">
    <a href="#">HOME</a>
    <a href="#">WHO WE ARE</a>
    <a href="#" class="is-active">WHAT WE OFFER</a>
    <a href="#">SUPPORT</a>
    <a href="#">CONTACTUS</a>
  </nav>

  <h1 class="hero-title">Business<br>Copiers/MFPs</h1>
  <p class="hero-text">The new Varo user interface lets you edit your documents, drag and rearrange files all with the slide of a finger. The 10.1" color LCD touch control panel is customizable to meet virtually all of your needs.</p>
  <a class="read-more">READ MORE</a>
  <div class="product-shot" role="img" aria-label="Product photo of a multifunction office copier with finisher and paper trays"></div>
  <div class="slider-dots"><span class="is-current"></span><span></span></div>

  <svg class="dome" width="1200" height="730" viewBox="0 0 1200 730" aria-hidden="true">
    <path d="M128 730 C 230 560, 420 538, 600 538 C 780 538, 970 560, 1080 730 Z" fill="var(--dome)"/>
  </svg>

  <div class="quick-links">
    <div class="quick-link" style="left:140px">
      <div class="icon"><span class="icon-brand">Hlumo</span></div>
      <span class="label">WHO ARE WE</span>
    </div>
    <div class="quick-link" style="left:384px">
      <div class="icon"><span class="icon-copier" role="img" aria-label="Small copier product image"></span></div>
      <span class="label">WHAT WE OFFER</span>
    </div>
    <div class="quick-link" style="left:618px">
      <div class="icon"><span class="icon-support" role="img" aria-label="Support agent with headset icon"></span></div>
      <span class="label">SUPPORT</span>
    </div>
    <div class="quick-link" style="left:856px">
      <div class="icon">
        <svg width="34" height="44" viewBox="0 0 24 24" aria-hidden="true"><path fill="var(--white)" d="M6.6 2.2c.6-.4 1.4-.2 1.8.4l2.2 3.4c.4.6.3 1.4-.3 1.8l-1.6 1.2c.9 2.3 2.6 4.6 4.6 6.2l1.5-1.1c.6-.4 1.4-.3 1.8.3l2.4 3.2c.4.6.3 1.4-.3 1.9l-1.6 1.2c-1 .7-2.3.8-3.4.2C9.2 18.6 5.3 13.5 4 8.1c-.3-1.2.1-2.5 1.1-3.3z"/></svg>
      </div>
      <span class="label">CONTACT US</span>
    </div>
  </div>

  <div class="footer-rule"></div>
  <p class="copyright">Copyrights 2013, All rights reserved by Hlumo, Inc.</p>
</div>
</body>
</html>
```